Will you marry me post card

I am just looking for a postcard to send my partner that will ask him to marry me.
I plan on creating about 200 of them and mailing them all at once so that he gets them all on the same day.
They should all be similar or could have a few different options.
I would like it simple, elegant, clean and crisp. No images, just text or icons

My only requirement is the text, "will you marry me?" in all lowercase -- any fonts, can be big, small, varying sizes, repeated, whole card, tiny space, don't care...just amazing design. BUT SIMPLE!

```html
<!DOCTYPE html>
<html lang="en">
<head>
<meta charset="utf-8">
<title>will you marry me? — postcard set</title>
<link rel="stylesheet" href="https://fonts.googleapis.com/css2?family=Quicksand:wght@500;600&family=Dancing+Script:wght@700&family=Cormorant+Garamond:wght@300&family=Josefin+Sans:wght@100;200&family=Kaushan+Script&display=swap">
<style>
  :root {
    --backdrop: #1b1b1b;
    --card: #f7f7f7;
    --card-edge: #e6e6e6;
    --ink: #121212;
  }
  * { box-sizing: border-box; margin: 0; padding: 0; }
  html, body {
    width: 1200px;
    height: 800px;
    overflow: hidden;
    background: var(--backdrop);
  }
  .card-set {
    width: 1200px;
    height: 800px;
    padding: 24px;
    display: grid;
    grid-template-columns: 1fr 1fr;
    grid-template-rows: 1fr 1fr;
    gap: 24px;
  }
  .postcard {
    background: var(--card);
    border: 1px solid var(--card-edge);
    color: var(--ink);
    display: flex;
    align-items: center;
    justify-content: center;
    overflow: hidden;
  }
  .message {
    display: flex;
    flex-direction: column;
    line-height: 1.1;
  }

  /* Variant: classic light serif around a script word */
  .postcard--classic .message { align-items: center; }
  .postcard--classic .lead {
    font-family: "Cormorant Garamond", serif;
    font-weight: 300;
    font-size: 60px;
    letter-spacing: 8px;
  }
  .postcard--classic .key {
    font-family: "Dancing Script", cursive;
    font-weight: 700;
    font-size: 120px;
    line-height: 1.15;
  }
  .postcard--classic .tail {
    font-family: "Cormorant Garamond", serif;
    font-weight: 300;
    font-size: 44px;
    letter-spacing: 6px;
  }

  /* Variant: thin geometric sans with a script word */
  .postcard--modern .message { align-items: flex-start; }
  .postcard--modern .lead {
    font-family: "Josefin Sans", sans-serif;
    font-weight: 200;
    font-size: 60px;
    letter-spacing: 12px;
    margin-left: 6px;
  }
  .postcard--modern .key {
    font-family: "Dancing Script", cursive;
    font-weight: 700;
    font-size: 130px;
    line-height: 1.15;
  }
  .postcard--modern .tail {
    font-family: "Josefin Sans", sans-serif;
    font-weight: 200;
    font-size: 44px;
    letter-spacing: 6px;
    align-self: flex-end;
  }

  /* Variant: geometric word with script accents */
  .postcard--geometric .message { align-items: stretch; }
  .postcard--geometric .lead {
    font-family: "Kaushan Script", cursive;
    font-size: 42px;
    text-align: right;
    margin-right: 10px;
  }
  .postcard--geometric .key {
    font-family: "Quicksand", sans-serif;
    font-weight: 500;
    font-size: 150px;
    letter-spacing: -2px;
    line-height: 1.2;
  }
  .postcard--geometric .tail {
    font-family: "Kaushan Script", cursive;
    font-size: 42px;
    margin-left: 14px;
  }

  /* Variant: heavier geometric word */
  .postcard--bold .message { align-items: flex-start; }
  .postcard--bold .lead {
    font-family: "Kaushan Script", cursive;
    font-size: 40px;
    margin-left: 8px;
  }
  .postcard--bold .key {
    font-family: "Quicksand", sans-serif;
    font-weight: 600;
    font-size: 150px;
    letter-spacing: -3px;
    line-height: 1.2;
  }
  .postcard--bold .tail {
    font-family: "Kaushan Script", cursive;
    font-size: 40px;
    align-self: flex-end;
    margin-right: 8px;
  }
</style>
</head>
<body>
  <main class="card-set">
    <section class="postcard postcard--classic">
      <p class="message"><span class="lead">will you</span><span class="key">marry</span><span class="tail">me?</span></p>
    </section>
    <section class="postcard postcard--modern">
      <p class="message"><span class="lead">will you</span><span class="key">marry</span><span class="tail">me?</span></p>
    </section>
    <section class="postcard postcard--geometric">
      <p class="message"><span class="lead">will you</span><span class="key">marry</span><span class="tail">me?</span></p>
    </section>
    <section class="postcard postcard--bold">
      <p class="message"><span class="lead">will you</span><span class="key">marry</span><span class="tail">me?</span></p>
    </section>
  </main>
</body>
</html>
```